Small corporate website template design

I need a couple templates designed for a small corporate website. The corporate site reflects the existence of the parent company which will own various brands/services that have their own websites, so it will mainly be used to present who we are, what we do, what is happening (news/events), how to contact us, link off to our other brand/service sites, as well as post information for public relations, investors, and job opportunities.

The company name is Velmoranth LLC (www.velmoranth-example.com), and the name is representative of stratified layers of interconnected digital services. The corporate site is not expected to generate a bunch of fanfare - that honor will be reserved for the externally linked brand/service sites.

The provided logo may be manipulated in color, size, shape, positioning, etc. to get it to fit with the design, but should be integrated in some way.

What we are looking for is a home page layout as well as a template for an inner page whereby the navigation/logo, etc may be diminished to some extent for the inner pages. We are also interested in reusable elements such as dividers, content containers, etc. in order to represent the types of information described above that we would like to present as described above.

We are particularly interested in consistency of design elements, conservative use of color (including consideration of accessibility concerns), judicious use of whitespace in favor of simplified messaging, and something lending itself well to internationalization/translation.

Target Market(s)

Small business owners, entrepreneurs (B2B)

Number of Pages Required

2 page

Font styles to use
Sans Serif

Requirements
Must have
• See the attached PDF with the logo concept, color swatches, and comparative sites.

```html
<!DOCTYPE html>
<html lang="en">
<head>
<meta charset="utf-8">
<title>Velmoranth LLC — Home</title>
<link rel="stylesheet" href="https://fonts.googleapis.com/css2?family=Montserrat:wght@500;600;700&family=Open+Sans:wght@400;600&display=swap">
<style>
  :root {
    --navy: #1c2d5a;
    --blue-accent: #4a7cbf;
    --link-blue: #1f55b8;
    --band-light: #2a55a6;
    --band-dark: #0b1c4c;
    --green: #6db31d;
    --green-footer: #78b82a;
    --page-bg: #f3f4f7;
    --text-dark: #333a44;
    --text-muted: #666c75;
    --white: #ffffff;
  }
  * { box-sizing: border-box; margin: 0; padding: 0; }
  html, body { width: 732px; height: 1200px; overflow: hidden; }
  body {
    position: relative;
    background: var(--white);
    font-family: "Open Sans", Arial, sans-serif;
    color: var(--text-dark);
  }
  .abs { position: absolute; }

  /* Header */
  .hero-bg {
    left: 0; top: 0; width: 732px; height: 430px;
    background: radial-gradient(ellipse at 70% 40%, #ffffff 0%, var(--page-bg) 70%, #e9ebef 100%);
  }
  .brand {
    left: 76px; top: 30px; display: flex; align-items: center; gap: 8px;
    font-family: "Montserrat", Arial, sans-serif; font-weight: 600; font-size: 18px; color: #1a1a1a;
  }
  .brand-mark { width: 30px; height: 30px; border-radius: 50%; background: #1a1a1a; }
  .main-nav { left: 264px; top: 32px; display: flex; gap: 21px; }
  .main-nav a {
    font-family: "Montserrat", Arial, sans-serif; font-size: 8.6px; font-weight: 500;
    color: #2b2f36; text-decoration: none; letter-spacing: .2px;
  }
  .main-nav a.is-active { color: var(--blue-accent); }

  .hero-title {
    left: 70px; top: 160px; font-family: "Montserrat", Arial, sans-serif; font-weight: 700;
    font-size: 20.5px; line-height: 25px; color: var(--navy); letter-spacing: .3px;
  }
  .hero-title .accent { color: var(--blue-accent); }
  .btn-solid {
    left: 70px; top: 251px; width: 106px; height: 30px; border-radius: 15px;
    background: var(--green); color: var(--white); font-family: "Montserrat", Arial, sans-serif;
    font-weight: 600; font-size: 10.5px; display: flex; align-items: center; justify-content: center;
  }
  .hero-visual {
    left: 390px; top: 75px; width: 275px; height: 275px; border-radius: 50%;
    background: radial-gradient(circle at 50% 45%, #8c3fd1 0%, #4a4fd0 30%, #36c4e0 55%, rgba(200,200,215,.35) 72%, rgba(243,244,247,0) 100%);
  }
  .slider-dots { left: 336px; top: 351px; display: flex; align-items: center; gap: 5px; }
  .slider-arrow { width: 12px; height: 12px; border-radius: 50%; background: #8a8f98; }
  .slider-dot { width: 5px; height: 5px; border-radius: 50%; background: #c2c5cb; }
  .slider-dot.is-active { background: #8a8f98; }

  /* Who we are */
  .band { left: 0; top: 370px; }
  .section-title {
    left: 0; width: 732px; text-align: center; font-family: "Montserrat", Arial, sans-serif;
    font-weight: 700; letter-spacing: .4px;
  }
  .who-title { top: 464px; font-size: 18.5px; color: var(--white); }
  .who-text {
    left: 136px; top: 500px; width: 460px; text-align: center; font-size: 8.8px; line-height: 15.2px;
    color: #e6ecf7;
  }
  .btn-outline {
    left: 307px; top: 573px; width: 106px; height: 30px; border-radius: 15px;
    border: 1.5px solid var(--white); color: var(--white); font-family: "Montserrat", Arial, sans-serif;
    font-weight: 600; font-size: 10.5px; display: flex; align-items: center; justify-content: center;
  }

  /* Blogs */
  .blogs-bg { left: 0; top: 700px; width: 732px; height: 280px; background: #f6f6f7; }
  .blogs-title { top: 708px; font-size: 16.5px; color: var(--green); }
  .blog-card {
    top: 743px; width: 185px; height: 209px; background: var(--white); border: 1px solid #c9ccd1;
  }
  .blog-image { position: absolute; left: 0; top: 0; width: 183px; height: 116px; }
  .img-code { background: linear-gradient(135deg, #0d1730, #1b3a5a 50%, #7a3a20); }
  .img-screen { background: linear-gradient(135deg, #8a98a6, #d8dde2 55%, #3f4b5a); }
  .img-team { background: linear-gradient(135deg, #5a4236, #a88a78 50%, #2c3440); }
  .blog-date {
    position: absolute; left: 6px; top: 126px; width: 35px; height: 35px; border-radius: 50%;
    background: var(--blue-accent); color: var(--white); text-align: center;
    font-family: "Montserrat", Arial, sans-serif; line-height: 1;
  }
  .blog-date .day { display: block; font-size: 13px; margin-top: 6px; }
  .blog-date .month { display: block; font-size: 8px; margin-top: 1px; }
  .blog-heading { position: absolute; left: 48px; top: 128px; font-size: 11px; color: #222; font-weight: 400; }
  .blog-excerpt { position: absolute; left: 48px; top: 146px; width: 130px; font-size: 7px; line-height: 11px; color: var(--text-muted); }
  .blog-more { position: absolute; left: 48px; top: 183px; font-size: 8px; font-weight: 600; color: var(--link-blue); }

  /* Footer */
  .footer-band { left: 0; top: 970px; }
  .footer-name {
    left: 78px; top: 1055px; width: 130px; text-align: center;
    font-family: "Montserrat", Arial, sans-serif; font-weight: 600; font-size: 15px; color: #a8d66f;
  }
  .social-list { left: 89px; top: 1108px; display: flex; gap: 4px; }
  .social-item { width: 21px; height: 21px; border-radius: 50%; border: 1.2px solid var(--white); }
  .footer-col { top: 1034px; }
  .footer-heading { font-family: "Montserrat", Arial, sans-serif; font-weight: 600; font-size: 10.5px; color: var(--white); margin-bottom: 12px; }
  .footer-links { list-style: none; }
  .footer-links li { font-size: 9.3px; color: var(--white); line-height: 18.6px; }
  .contact-list { list-style: none; }
  .contact-list li { display: flex; align-items: center; gap: 8px; font-size: 9.3px; color: var(--white); line-height: 18.6px; }
  .contact-list svg { width: 11px; height: 11px; flex: none; }
  .footer-rule { left: 72px; top: 1166px; width: 580px; height: 1px; background: rgba(255,255,255,.45); }
  .copyright { left: 0; top: 1177px; width: 732px; text-align: center; font-size: 7px; color: #e9f4dc; }
</style>
</head>
<body>

  <!-- Hero -->
  <div class="abs hero-bg"></div>
  <div class="abs brand"><span class="brand-mark"></span>Velmoranth</div>
  <nav class="abs main-nav">
    <a class="is-active" href="#">HOME</a>
    <a href="#">ABOUT US</a>
    <a href="#">WHY WE ARE</a>
    <a href="#">WHAT WE DO</a>
    <a href="#">NEWS</a>
    <a href="#">JOBS</a>
    <a href="#">CONTACT</a>
  </nav>
  <h1 class="abs hero-title"><span class="accent">ADAPTIVE SOFTWARE</span><br>TECHNOLOGY FOR<br>THE DIGITAL REVOLUTION</h1>
  <a class="abs btn-solid">Learn More</a>
  <div class="abs hero-visual" role="img" aria-label="Illustration of a glowing network sphere of connected nodes in purple and cyan"></div>
  <div class="abs slider-dots">
    <span class="slider-arrow"></span>
    <span class="slider-dot is-active"></span><span class="slider-dot"></span><span class="slider-dot"></span><span class="slider-dot"></span>
    <span class="slider-arrow"></span>
  </div>

  <!-- Who we are -->
  <svg class="abs band" width="732" height="336" viewBox="0 0 732 336" role="img" aria-label="Deep blue band with a digital network landscape">
    <defs>
      <linearGradient id="bandFill" x1="0" y1="1" x2="1" y2="0">
        <stop offset="0" stop-color="var(--band-light)"/>
        <stop offset="1" stop-color="var(--band-dark)"/>
      </linearGradient>
    </defs>
    <polygon points="0,3 732,52 732,336 0,286" fill="url(#bandFill)"/>
  </svg>
  <h2 class="abs section-title who-title">WHO WE ARE</h2>
  <p class="abs who-text">magna nisl nec elit Praesent elementum elit at tellus nec ultricies sit amet porttitor mattis enim In massa libero interdum nec interdum vel blandit sed nulla In ullamcorper est eget tempor cursus neque mi consectetuer mi a ultricies massa est sed nisl Class aptent taciti sociosqu ad litora torquent per conubia nostra per inceptos hymenaeos Proin nulla arcu nonummy luctus dictum ege</p>
  <a class="abs btn-outline">Learn More</a>

  <!-- Blogs -->
  <div class="abs blogs-bg"></div>
  <h2 class="abs section-title blogs-title">OUR BLOGS</h2>

  <article class="abs blog-card" style="left:72px">
    <div class="blog-image img-code" role="img" aria-label="Photo of code on a dark screen with a network graphic"></div>
    <div class="blog-date"><span class="day">20</span><span class="month">MAY</span></div>
    <h3 class="blog-heading">Your Blog Title here</h3>
    <p class="blog-excerpt">netus et malesuada fames ac turpis egestas Cras id elit Integer quis urna Ut ante enim dapibus males</p>
    <a class="blog-more">READ MORE</a>
  </article>

  <article class="abs blog-card" style="left:270px">
    <div class="blog-image img-screen" role="img" aria-label="Photo of colleagues working together at a computer"></div>
    <div class="blog-date"><span class="day">28</span><span class="month">APR</span></div>
    <h3 class="blog-heading">Your Blog Title here</h3>
    <p class="blog-excerpt">netus et malesuada fames ac turpis egestas Cras id elit Integer quis urna Ut ante enim dapibus males</p>
    <a class="blog-more">READ MORE</a>
  </article>

  <article class="abs blog-card" style="left:468px">
    <div class="blog-image img-team" role="img" aria-label="Photo of a development team in an office"></div>
    <div class="blog-date"><span class="day">30</span><span class="month">APR</span></div>
    <h3 class="blog-heading">Your Blog Title here</h3>
    <p class="blog-excerpt">netus et malesuada fames ac turpis egestas Cras id elit Integer quis urna Ut ante enim dapibus males</p>
    <a class="blog-more">READ MORE</a>
  </article>

  <!-- Footer -->
  <svg class="abs footer-band" width="732" height="230" viewBox="0 0 732 230">
    <polygon points="0,35 732,0 732,230 0,230" fill="var(--green-footer)"/>
  </svg>
  <div class="abs footer-name">Velmoranth</div>
  <div class="abs social-list">
    <span class="social-item"></span><span class="social-item"></span><span class="social-item"></span><span class="social-item"></span>
  </div>

  <div class="abs footer-col" style="left:224px">
    <h4 class="footer-heading">QUICK LINKS</h4>
    <ul class="footer-links"><li>About Us</li><li>What We Do</li><li>Who We Are</li><li>Why Us</li></ul>
  </div>
  <div class="abs footer-col" style="left:349px">
    <h4 class="footer-heading">RESOURCES</h4>
    <ul class="footer-links"><li>News &amp; Blogs</li><li>Team</li><li>Contact Us</li></ul>
  </div>
  <div class="abs footer-col" style="left:468px">
    <h4 class="footer-heading">CONTACT US</h4>
    <ul class="contact-list">
      <li><svg viewBox="0 0 12 12"><path d="M6 0.8a3.6 3.6 0 0 0-3.6 3.6C2.4 7.2 6 11.4 6 11.4s3.6-4.2 3.6-7A3.6 3.6 0 0 0 6 0.8zm0 5a1.4 1.4 0 1 1 0-2.8 1.4 1.4 0 0 1 0 2.8z" fill="#fff"/></svg>48 Larkspur Avenue, Suite 210, Brenhollow 55012</li>
      <li><svg viewBox="0 0 12 12"><path d="M2.5 1h2l1 2.6-1.3 1a6.5 6.5 0 0 0 3.2 3.2l1-1.3L11 7.5v2A1.2 1.2 0 0 1 9.8 10.8 9.3 9.3 0 0 1 1.2 2.2 1.2 1.2 0 0 1 2.5 1z" fill="none" stroke="#fff" stroke-width="0.9"/></svg>555.014.7720</li>
      <li><svg viewBox="0 0 12 12"><rect x="1" y="2.5" width="10" height="7" fill="none" stroke="#fff" stroke-width="0.9"/><path d="M1 2.5l5 4 5-4" fill="none" stroke="#fff" stroke-width="0.9"/></svg>info@velmoranth-example.com</li>
    </ul>
  </div>
  <div class="abs footer-rule"></div>
  <p class="abs copyright">© 2018 Company Name &nbsp;All right reserved</p>

</body>
</html>
```